Your Health, Your Time, Your Way: Personalized, Concierge Care Elevated to Modern Medicine

We need to incorporate an image of our new doctor (Dr. Malvina Okoruwe, MD) with our office logo ( Harborline Family Clinic) and dialogue that shows how simple it is to schedule a free consult and learn what our office has to offer patients. The colors should be consistent with our website- the CMYK codes will be attached for your use below. The font should be easy to read. The text should be clear, and convey value to the patient for chosing us over anyone else ( we offer primary care, preventive medicine, urgen care and functional medicine with 24 hour direct access to care with some of our strengths including focus on individualized care, cutting edge medicine, blended functional and traditional style. We aim to transform lives through patient centered innovative and individualized care plan. I have attached a "mock" image but the details ( office address, name, phone number are incorrect) The correct info is Harborline Family Clinic 4187 Wrenfield Ave Suite 214, Clearwater, FL 33759 and phone number (727)482-3095. A possible hook could read: welcoming new patients now- Your Health, Your Time, Your Way: Personalized Care Meets Modern Medicine
Updates

I did not realize that there was a tab with more information to fill for the designers to see, or for me to upload the basic information they need to create the design.

Target Market(s)

Patients over 18 years of age with interest in longevity, functional and traditional medicine; the postcards will be mailed to our CURRENT patients, and they are a reminder of what we do, new patient availability AND a request for them to refer friends or families

Industry/Entity Type

medical

Font styles to use
Sans Serif

Colors

Designer to choose colors to be used in the design.

Requirements
Must have
• simple reminder to current patients of what we offer, and a call to action for our patients to refer friends and family for same level of excellence;consistency with brand ( see business card and cmyx codes for colors);photo of new physician; logo Harborline Family Clinic, web site (https://harborlinefamilyclinic.net); Must clearly express accepting new patients; simple to call/email to schedule free consultation;; include our email (office@harborlinefamilyclinic.org), phone number (727)482-3095; our address 4187 Wrenfield Ave Suite 214, Clearwater, FL 33759
Nice to have
• photo of our new physician ( in blue jacket: Dr. Malvina Okoruwe, MD) should not take up too much space
Should not have
• clutter, or close text; full sentences( bulleted text preferred)

```html
<!DOCTYPE html>
<html lang="en">
<head>
<meta charset="utf-8">
<title>Harborline Family Clinic – Postcard</title>
<link href="https://fonts.googleapis.com/css2?family=Outfit:wght@300;400;600;700;800&family=Montserrat:wght@500;800;900&display=swap" rel="stylesheet">
<style>
  :root{
    --backdrop:#222222;
    --slate:#5f7189;
    --slate-dark:#4f6178;
    --ink:#111111;
    --white:#ffffff;
    --arch-top:#97a1b4;
    --arch-bottom:#f1f2f5;
  }
  *{margin:0;padding:0;box-sizing:border-box}
  html,body{width:1200px;height:1200px;overflow:hidden;background:var(--backdrop)}
  .postcard{position:absolute;left:53px;top:296px;width:1094px;height:608px;background:var(--white);font-family:"Outfit",sans-serif;color:var(--white)}
  .hero{position:absolute;left:0;top:0;width:1094px;height:473px;background:linear-gradient(100deg,var(--slate) 60%,var(--slate-dark));overflow:hidden}
  .headline{position:absolute;left:34px;top:20px;font-weight:800;font-size:33px;color:var(--ink);letter-spacing:.2px;line-height:1}
  .subline{position:absolute;left:34px;top:56px;font-weight:700;font-size:17.5px;line-height:1}
  .section-title{position:absolute;left:34px;font-weight:600;font-size:19.5px;color:var(--ink);line-height:1}
  .offer-title{top:98px}
  .access-title{top:200px}
  .check-list{position:absolute;list-style:none;font-weight:300;font-size:19.5px;line-height:25px}
  .check-list li{display:flex;align-items:center;gap:11px;white-space:nowrap}
  .check-list li svg{flex:none;width:16px;height:16px}
  .services-a{left:32px;top:121px}
  .services-b{left:206px;top:121px}
  .strengths{left:32px;top:225px}
  .strengths .wrap{align-items:flex-start;white-space:normal;width:480px}
  .strengths .wrap svg{margin-top:5px}
  .divider{position:absolute;left:34px;top:186px;width:552px;height:1px;background:rgba(255,255,255,.75)}
  .referral{position:absolute;left:0;top:356px;width:585px;height:65px;background:var(--white);border-radius:0 12px 12px 0}
  .referral-badge{position:absolute;left:31px;top:344px;width:93px;height:93px}
  .referral-text{position:absolute;left:135px;top:365px;font-weight:700;font-size:22.5px;line-height:25px;white-space:nowrap}
  .referral-text .lead{color:var(--slate)}
  .referral-text .strong{color:var(--ink)}
  .doctor-photo{position:absolute;left:641px;top:110px;width:428px;height:311px;border-radius:214px 214px 0 0;background:linear-gradient(180deg,var(--arch-top),var(--arch-bottom))}
  .doctor-name{position:absolute;left:648px;top:428px;font-size:28.5px;font-weight:300;white-space:nowrap;line-height:1.3}
  .doctor-name b{font-weight:700}
  .footer{position:absolute;left:0;top:473px;width:1094px;height:135px;color:var(--ink)}
  .brand{position:absolute;left:30px;top:34px;width:120px;font-family:"Outfit",sans-serif;font-weight:600;font-size:19px;line-height:22px;color:var(--ink)}
  .footer-rule{position:absolute;left:162px;top:12px;height:112px;border-left:2px dotted var(--ink)}
  .cta{position:absolute;left:171px;top:13px;font-family:"Montserrat",sans-serif;font-weight:900;font-size:22.5px;white-space:nowrap;letter-spacing:.2px}
  .cta .accent{color:var(--slate)}
  .contact{position:absolute;left:171px;width:923px;text-align:center;font-family:"Montserrat",sans-serif;font-weight:500;font-size:23px;white-space:nowrap;display:flex;justify-content:center;align-items:center;gap:7px}
  .contact svg{width:20px;height:20px;flex:none}
  .contact-a{top:49px}
  .contact-b{top:85px}
  .contact .web{color:var(--slate)}
</style>
</head>
<body>
<main class="postcard">
  <section class="hero">
    <h1 class="headline">YOUR HEALTH, YOUR TIME, YOUR WAY</h1>
    <p class="subline">PERSONALIZED CONCIERGE CARE ELEVATED TO MODERN MEDICINE</p>

    <h2 class="section-title offer-title">We offer a range of services to meet your healthcare needs</h2>
    <ul class="check-list services-a">
      <li><svg viewBox="0 0 16 16"><circle cx="8" cy="8" r="7" fill="none" stroke="#fff" stroke-width="1.3"/><path d="M4.8 8.2l2.2 2.1 4.2-4.4" fill="none" stroke="#fff" stroke-width="1.3"/></svg>Primary Care</li>
      <li><svg viewBox="0 0 16 16"><circle cx="8" cy="8" r="7" fill="none" stroke="#fff" stroke-width="1.3"/><path d="M4.8 8.2l2.2 2.1 4.2-4.4" fill="none" stroke="#fff" stroke-width="1.3"/></svg>Urgent Care</li>
    </ul>
    <ul class="check-list services-b">
      <li><svg viewBox="0 0 16 16"><circle cx="8" cy="8" r="7" fill="none" stroke="#fff" stroke-width="1.3"/><path d="M4.8 8.2l2.2 2.1 4.2-4.4" fill="none" stroke="#fff" stroke-width="1.3"/></svg>Preventive Medicine</li>
      <li><svg viewBox="0 0 16 16"><circle cx="8" cy="8" r="7" fill="none" stroke="#fff" stroke-width="1.3"/><path d="M4.8 8.2l2.2 2.1 4.2-4.4" fill="none" stroke="#fff" stroke-width="1.3"/></svg>Functional Medicine</li>
    </ul>

    <div class="divider"></div>

    <h2 class="section-title access-title">With 24-hour direct access to care, we emphasize</h2>
    <ul class="check-list strengths">
      <li><svg viewBox="0 0 16 16"><circle cx="8" cy="8" r="7" fill="none" stroke="#fff" stroke-width="1.3"/><path d="M4.8 8.2l2.2 2.1 4.2-4.4" fill="none" stroke="#fff" stroke-width="1.3"/></svg>Individualized treatment plans</li>
      <li><svg viewBox="0 0 16 16"><circle cx="8" cy="8" r="7" fill="none" stroke="#fff" stroke-width="1.3"/><path d="M4.8 8.2l2.2 2.1 4.2-4.4" fill="none" stroke="#fff" stroke-width="1.3"/></svg>Cutting-edge medical practices</li>
      <li class="wrap"><svg viewBox="0 0 16 16"><circle cx="8" cy="8" r="7" fill="none" stroke="#fff" stroke-width="1.3"/><path d="M4.8 8.2l2.2 2.1 4.2-4.4" fill="none" stroke="#fff" stroke-width="1.3"/></svg><span>A blend of functional and traditional medicine approaches</span></li>
    </ul>

    <div class="referral"></div>
    <svg class="referral-badge" viewBox="0 0 93 93" aria-hidden="true">
      <circle cx="46.5" cy="46.5" r="45" fill="#fff"/>
      <circle cx="46.5" cy="46.5" r="43" fill="none" stroke="#5f7189" stroke-width="2"/>
      <circle cx="33" cy="27" r="9" fill="#5f7189"/>
      <path d="M18 58c0-13 6-20 15-20s14 5 15 10v10z" fill="#5f7189"/>
      <circle cx="57" cy="40" r="10" fill="#5f7189"/>
      <path d="M40 73c0-14 7-21 17-21s17 7 17 21z" fill="#5f7189"/>
      <path d="M37 78c-6-3-9-9-8-16" fill="none" stroke="#5f7189" stroke-width="3"/>
      <path d="M24 64l5-6 5 6" fill="none" stroke="#5f7189" stroke-width="3"/>
    </svg>
    <p class="referral-text"><span class="lead">REFER YOUR FRIENDS AND FAMILY TO</span><br><span class="strong">EXPERIENCE THE SAME EXCELLENCE</span></p>

    <div class="doctor-photo" role="img" aria-label="Portrait photograph of Dr. Malvina Okoruwe, MD, smiling, in a dark blue jacket"></div>
    <p class="doctor-name">DR. MALVINA <b>OKORUWE, MD</b></p>
  </section>

  <footer class="footer">
    <p class="brand">Harborline Family Clinic</p>
    <div class="footer-rule"></div>
    <p class="cta"><span class="accent">NOW ACCEPTING NEW PATIENTS - </span>SCHEDULE A FREE CONSULTATION</p>
    <p class="contact contact-a">
      <svg viewBox="0 0 20 20" aria-hidden="true"><path d="M5 2l3 4-2 2c1 3 3 5 6 6l2-2 4 3-2 3C9 18 2 11 2 4z" fill="none" stroke="#5f7189" stroke-width="1.6"/></svg>
      <span>(727)482-3095 |</span>
      <svg viewBox="0 0 20 20" aria-hidden="true"><path d="M10 18s-5-6-5-10a5 5 0 0 1 10 0c0 4-5 10-5 10z" fill="none" stroke="#5f7189" stroke-width="1.6"/><circle cx="10" cy="8" r="2" fill="#5f7189"/></svg>
      <span>4187 Wrenfield Ave Suite 214, Clearwater, FL 33759</span>
    </p>
    <p class="contact contact-b">
      <svg viewBox="0 0 20 20" aria-hidden="true"><rect x="2" y="5" width="16" height="11" fill="none" stroke="#5f7189" stroke-width="1.6"/><path d="M2 5l8 6 8-6" fill="none" stroke="#5f7189" stroke-width="1.6"/></svg>
      <span>office@harborlinefamilyclinic.org |</span>
      <svg viewBox="0 0 20 20" aria-hidden="true"><circle cx="10" cy="10" r="7.5" fill="none" stroke="#5f7189" stroke-width="1.4"/><ellipse cx="10" cy="10" rx="3.5" ry="7.5" fill="none" stroke="#5f7189" stroke-width="1.2"/><path d="M2.5 10h15" stroke="#5f7189" stroke-width="1.2"/></svg>
      <span>www.<span class="web">harborlinefamilyclinic</span>.net</span>
    </p>
  </footer>
</main>
</body>
</html>
```